A starter web site for the Ridgeway Digital Shield Association. Our target market are companies that use cyber security products and services and those who provide them.

Target Market(s)

Companies that provide cyber security products and services.

Industry/Entity Type

Security

Coding

Coded - Design and coding required

Number of Pages Required

5+ page

Font styles to use
Serif

Requirements
Must have
• We need the site to have an editor so we can add content, pictures and links to video on Clipzo.
Nice to have
• If possible a way to collect names of people interested in joining the organization. that falls into a excel spreadsheet.
Should not have
• Hard to read characters

```html
<!DOCTYPE html>
<html lang="en">
<head>
<meta charset="utf-8">
<title>Ridgeway Digital Shield Association</title>
<link rel="stylesheet" href="https://fonts.googleapis.com/css2?family=Titillium+Web:wght@400;600&family=Open+Sans:wght@400;600;700&display=swap">
<style>
:root{
  --red:#c01f2f;
  --red-dark:#a81a28;
  --nav-active:#6d6d6d;
  --ink:#333;
  --muted:#666;
  --light:#ececec;
  --footer:#e8e8e8;
  --black:#111;
  --yellow:#f5cf12;
  --blue:#1372c0;
  --pink:#e8305a;
}
*{margin:0;padding:0;box-sizing:border-box}
html,body{width:678px;height:1200px;overflow:hidden;background:#fff}
body{font-family:"Open Sans",sans-serif;color:var(--ink);position:relative}
.heading{font-family:"Titillium Web",sans-serif;font-weight:600}
.topline{position:absolute;top:0;left:0;width:678px;height:3px;background:var(--red)}
.site-header{position:absolute;top:3px;left:0;width:678px;height:56px;background:#fff}
.brand{position:absolute;left:56px;top:10px;display:flex;align-items:center;gap:9px}
.brand-mark{width:30px;height:30px;border-radius:50%;background:var(--red)}
.brand-name{font-family:"Titillium Web",sans-serif;font-weight:600;color:var(--red);font-size:12.5px;line-height:13px;text-transform:uppercase;letter-spacing:.3px}
.main-nav{position:absolute;top:59px;left:0;width:678px;height:37px;background:var(--red);display:flex;padding-left:56px}
.main-nav a{color:#fff;text-decoration:none;font-size:7.5px;line-height:37px;height:37px}
.main-nav .active{background:var(--nav-active);width:86px;text-align:center}
.main-nav a:nth-child(2){margin-left:10px}
.main-nav a:nth-child(3){margin-left:43px}
.main-nav a:nth-child(4){margin-left:44px}
.main-nav a:nth-child(5){margin-left:44px}
.main-nav a:nth-child(6){margin-left:45px}
.hero{position:absolute;top:96px;left:0;width:678px;height:305px;
  background:radial-gradient(ellipse 230px 170px at 260px 150px,#c9a55a 0%,#a88843 45%,rgba(60,80,110,0) 75%),linear-gradient(135deg,#1f3550 0%,#4a6a8c 50%,#1d3350 100%)}
.hero-arrow{position:absolute;top:136px;width:18px;height:18px;border-radius:50%;background:#fff;display:flex;align-items:center;justify-content:center}
.hero-dots{position:absolute;top:286px;left:321px;display:flex;gap:4px}
.hero-dots span{width:8px;height:8px;border-radius:50%;border:1.5px solid #222;background:#fff}
.hero-dots .on{background:var(--pink);border-color:var(--pink)}
.mission{position:absolute;top:401px;left:0;width:678px;height:177px;background:#fff}
.mission h2{position:absolute;left:56px;top:13px;color:var(--red);font-size:14px}
.body-text{font-size:6.6px;line-height:13.6px;color:var(--muted)}
.mission p{position:absolute;left:57px;top:36px;width:326px}
.mission-image{position:absolute;left:393px;top:10px;width:228px;height:147px;background:linear-gradient(120deg,#2a6b8a 0%,#3c8ec0 45%,#6a4a8c 100%)}
.services{position:absolute;top:578px;left:0;width:678px;height:239px;background:linear-gradient(90deg,#3a2e28 0%,#5b4a40 50%,#3d332c 100%)}
.services h2{position:absolute;top:12px;width:100%;text-align:center;color:#fff;font-size:16.5px}
.service{position:absolute;top:60px;width:170px;text-align:center}
.service-icon{width:72px;height:72px;border-radius:50%;border:2px solid #fff;margin:0 auto;display:flex;align-items:center;justify-content:center}
.service h3{color:#fff;font-size:10px;margin-top:10px}
.service p{color:#fff;font-size:6.6px;font-weight:700;line-height:13.6px;margin-top:4px}
.service .more{font-size:6.6px;font-weight:700;margin-top:1px;display:block;text-decoration:none}
.how{position:absolute;top:817px;left:0;width:678px;height:165px;background:var(--light)}
.video{position:absolute;left:56px;top:16px;width:217px;height:128px;background:linear-gradient(135deg,#0f2c5c 0%,#2c5d9c 50%,#0c2246 100%)}
.video-bar{position:absolute;left:3px;right:3px;bottom:3px;height:19px;background:rgba(10,20,40,.8);display:flex;align-items:center;gap:6px;padding:0 6px}
.video-bar .track{flex:1;height:3px;background:#445a78}
.how h2{position:absolute;left:288px;top:20px;color:var(--red);font-size:14px}
.how p{position:absolute;left:288px;top:44px;width:334px}
.newsletter{position:absolute;top:982px;left:0;width:678px;height:55px;background:var(--red)}
.newsletter h2{position:absolute;left:82px;top:16px;color:#fff;font-size:14px;font-weight:400}
.email{position:absolute;left:179px;top:13px;width:302px;height:26px;background:#fff;border-radius:3px;font-size:7.5px;font-style:italic;color:#444;padding:0 9px;line-height:26px}
.email svg{position:absolute;right:8px;top:7px}
.subscribe{position:absolute;left:493px;top:13px;width:128px;height:26px;background:#5a5a5a;border-radius:3px;color:#fff;font-family:"Titillium Web",sans-serif;font-size:11px;text-align:center;line-height:26px}
.site-footer{position:absolute;top:1037px;left:0;width:678px;height:112px;background:var(--footer)}
.foot-col{position:absolute;top:18px}
.foot-col h4{font-family:"Titillium Web",sans-serif;font-weight:600;font-size:8.5px;color:#222;margin-bottom:5px}
.foot-col li{list-style:none;font-size:6.4px;line-height:13.6px;color:#555}
.foot-brand{position:absolute;right:57px;top:18px;text-align:right}
.foot-brand .brand-row{display:flex;align-items:center;gap:5px;justify-content:flex-end;margin-top:7px}
.foot-brand .brand-mark{width:18px;height:18px}
.foot-brand .brand-name{font-size:7px;line-height:8px;text-align:left}
.copyright{position:absolute;top:1149px;left:0;width:678px;height:51px;background:var(--black);color:#fff;font-size:6.8px;font-weight:600;text-align:center;line-height:51px}
</style>
</head>
<body>
<div class="topline"></div>
<header class="site-header">
  <div class="brand">
    <span class="brand-mark"></span>
    <span class="brand-name">Ridgeway Digital<br>Shield Association</span>
  </div>
</header>
<nav class="main-nav">
  <a class="active">Home</a>
  <a>About Us</a>
  <a>Membership Fees and Benefits</a>
  <a>Education</a>
  <a>Events</a>
  <a>Research Center</a>
</nav>
<section class="hero" role="img" aria-label="Gold padlock over a field of glowing binary code">
  <span class="hero-arrow" style="left:13px"><svg width="8" height="8" viewBox="0 0 8 8"><path d="M5.5 1 2.5 4l3 3" fill="none" stroke="#222" stroke-width="1.6"/></svg></span>
  <span class="hero-arrow" style="left:636px"><svg width="8" height="8" viewBox="0 0 8 8"><path d="M2.5 1l3 3-3 3" fill="none" stroke="#222" stroke-width="1.6"/></svg></span>
  <div class="hero-dots"><span class="on"></span><span></span><span></span></div>
</section>
<section class="mission">
  <h2 class="heading">Our Mission</h2>
  <p class="body-text">Lorem ipsum dolor sit amet, consectetuer adipiscing elit, sed diam nonummy nibh euismod tincidunt ut laoreet dolore magna aliquam erat volutpat. Ut wisi enim ad minim veniam, quis nostrud exerci tation ullamcorper suscipit lobortis nisl ut aliquip ex ea commodo consequat. Lorem ipsum dolor sit amet, consectetuer adipiscing elit, sed diam nonummy nibh euismod tincidunt ut laoreet dolore magna aliquam erat volutpat. Ut wisi enim ad minim veniam, quis nostrud exerci tation ullamcorper suscipit lobortis nisl ut aliquip ex ea commodo consequat. Lorem ipsum dolor sit amet, consectetuer adipiscing elit, sed diam nonummy nibh euismod tincidunt ut laoreet dolore magna aliquam erat volutpat. Ut wisi enim ad minim veniam, quis nostrud exerci tation ullamcorper suscipit lobortis nisl ut aliquip ex ea commodo consequat.</p>
  <div class="mission-image" role="img" aria-label="Glowing blue padlock formed from binary digits"></div>
</section>
<section class="services">
  <h2 class="heading">Services</h2>
  <div class="service" style="left:62px">
    <div class="service-icon" style="background:#d9283f">
      <svg width="30" height="30" viewBox="0 0 30 30" fill="none" stroke="#fff" stroke-width="2.6" stroke-linecap="round"><rect x="11" y="3" width="8" height="15" rx="4" fill="#fff"/><path d="M7 14a8 8 0 0 0 16 0M15 22v5M10 27h10"/></svg>
    </div>
    <h3 class="heading">Target Members</h3>
    <p>Lorem ipsum dolor sit amet, consectetuer adipiscing elit, sed diam nonummy nibh euismod tincidunt ut laoreet at.</p>
    <a class="more" style="color:#e8305a">Read more</a>
  </div>
  <div class="service" style="left:264px">
    <div class="service-icon" style="background:var(--yellow)">
      <svg width="38" height="26" viewBox="0 0 38 26" fill="#fff"><circle cx="19" cy="6" r="5"/><circle cx="8" cy="8" r="4"/><circle cx="30" cy="8" r="4"/><path d="M10 24c0-7 4-11 9-11s9 4 9 11z"/><path d="M1 23c0-6 3-9 7-9 2 0 3 .5 4 1.5-2 2-3 5-3 7.5zM37 23c0-6-3-9-7-9-2 0-3 .5-4 1.5 2 2 3 5 3 7.5z"/></svg>
    </div>
    <h3 class="heading">Programming</h3>
    <p>Lorem ipsum dolor sit amet, consectetuer adipiscing elit, sed diam nonummy nibh euismod tincidunt ut laoreet at.</p>
    <a class="more" style="color:var(--yellow)">Read more</a>
  </div>
  <div class="service" style="left:453px">
    <div class="service-icon" style="background:var(--blue)">
      <svg width="30" height="32" viewBox="0 0 30 32" fill="none" stroke="#fff" stroke-width="2"><rect x="5" y="4" width="15" height="25" rx="2"/><path d="M9 14h3l5-4v12l-5-4H9z" fill="#fff"/><path d="M22 10l4-3M23 16h5M22 22l4 3" stroke-linecap="round"/></svg>
    </div>
    <h3 class="heading">Benefits</h3>
    <p>Lorem ipsum dolor sit amet, consectetuer adipiscing elit, sed diam nonummy nibh euismod tincidunt ut laoreet at.</p>
    <a class="more" style="color:var(--blue)">Read more</a>
  </div>
</section>
<section class="how">
  <div class="video" role="img" aria-label="Clipzo video: hacker at a keyboard surrounded by floating security keywords">
    <div class="video-bar">
      <svg width="10" height="10" viewBox="0 0 10 10"><path d="M2 1l7 4-7 4z" fill="#fff"/></svg>
      <span class="track"></span>
    </div>
  </div>
  <h2 class="heading">How It Works</h2>
  <p class="body-text">Lorem ipsum dolor sit amet, consectetuer adipiscing elit, sed diam nonummy nibh euismod tincidunt ut laoreet dolore magna aliquam erat volutpat. Ut wisi enim ad minim veniam, quis nostrud exerci tation ullamcorper suscipit lobortis nisl ut aliquip ex ea commodo consequat. Lorem ipsum dolor sit amet, consectetuer adipiscing elit, sed diam nonummy nibh euismod tincidunt ut laoreet dolore magna aliquam erat volutpat. Ut wisi enim ad minim veniam, quis nostrud exerci tation ullamcorper suscipit lobortis nisl ut aliquip ex ea commodo consequat. Lorem ipsum dolor sit amet, consectetuer adipiscing elit, sed diam nonummy nibh euismod tincidunt ut laoreet dolore magna aliquam erat volutpat. Ut wisi enim ad minim veniam, quis nostrud exerci tation ullamcorper suscipit</p>
</section>
<section class="newsletter">
  <h2 class="heading">Newletters</h2>
  <div class="email">Enter Your Email
    <svg width="16" height="11" viewBox="0 0 16 11"><rect width="16" height="11" fill="#999"/><path d="M0 0l8 6 8-6" fill="none" stroke="#fff" stroke-width="1.2"/></svg>
  </div>
  <div class="subscribe">Subscribe</div>
</section>
<footer class="site-footer">
  <div class="foot-col" style="left:56px">
    <h4>About Us</h4>
    <ul><li>Home</li><li>Our Team</li><li>Our Work</li><li>Insight Articles</li><li>News</li></ul>
  </div>
  <div class="foot-col" style="left:156px">
    <h4>Our Services</h4>
    <ul><li>Brand &amp; Product Positioning</li><li>System 1 Research</li><li>Innovation</li><li>Hispanic Marketing</li></ul>
  </div>
  <div class="foot-col" style="left:334px">
    <h4>Contact Us Today</h4>
    <ul><li>218 Harbor Line Ave., Suite 310</li><li>Millbrook, CA 90455</li><li>T. 555-012-4870</li><li>hello@northgatestudio.example</li></ul>
  </div>
  <div class="foot-brand">
    <h4 class="heading" style="font-size:8.5px;color:#222">Follow The Northgate Studio</h4>
    <div class="brand-row"><span class="brand-mark"></span><span class="brand-name">Ridgeway Digital<br>Shield Association</span></div>
  </div>
</footer>
<div class="copyright">© 2014 Ridgeway Digital Shield Association- All Rights Reserved</div>
</body>
</html>
```